Lakeshore Vision Associates, P.C.
Diseases and Surgeries of the Retina, Macula and Vitreous
Lakeshore Vision Associates, P.C. - Medical
Creative Brief
Professional
Peter R. Haldane, MD
Birchwood Medical Tower 4215 N. Lindon Suite 812 Wexmore, IL 60952
peter@lakeshorevsa.com
www.lakeshorevsa.com
Appointment Date: MM/DD/YYYY at ____________am ___________pm Please telephone in advance if you will be unable to keep the appointment

```html
<!DOCTYPE html>
<html lang="en">
<head>
<meta charset="utf-8">
<title>Lakeshore Vision Associates – Stationery</title>
<link href="https://fonts.googleapis.com/css2?family=Cinzel:wght@600&family=Open+Sans:wght@400;600&display=swap" rel="stylesheet">
<style>
:root{
  --bg-top:#5a5a5a;
  --bg-bottom:#1e1e1e;
  --paper:#ffffff;
  --orange:#f07a14;
  --orange-deep:#c2470a;
  --orange-light:#fbb04a;
  --ink:#4a4a4a;
  --ink-soft:#8a8a8a;
  --ink-light:#d8d8d8;
  --card-dark:#151515;
}
*{margin:0;padding:0;box-sizing:border-box}
html,body{width:1200px;height:281px;overflow:hidden}
body{
  position:relative;
  background:radial-gradient(ellipse at 50% 20%,var(--bg-top),var(--bg-bottom) 80%);
  font-family:"Open Sans",Arial,sans-serif;
  color:var(--ink);
}
.piece{position:absolute;background:var(--paper);box-shadow:0 2px 6px rgba(0,0,0,.5)}
.brand{display:flex;align-items:center;gap:5px}
.brand-mark{border-radius:50%;background:var(--ink-soft);flex:none}
.brand-name{font-family:"Cinzel",Georgia,serif;font-weight:600;color:var(--ink);letter-spacing:.08em;text-transform:uppercase;line-height:1.2}
.small{font-size:3px;line-height:1.4;color:var(--ink-soft)}

/* main logo */
.hero-logo{position:absolute;left:82px;top:84px;gap:8px;align-items:flex-start}
.hero-logo .brand-mark{width:10px;height:10px;background:var(--ink-light);margin-top:3px}
.hero-logo .brand-name{color:#f2f2f2;font-size:13px;width:150px}
.hero-logo .tagline{font-size:5px;color:#bdbdbd;margin-top:4px;letter-spacing:.04em}

/* business cards */
.card{width:78px;height:46px;padding:5px}
.card .brand-mark{width:5px;height:5px}
.card .brand-name{font-size:4px;width:60px}
.card-front{left:12px;top:166px}
.card-back{left:94px;top:166px}
.card-back .name{font-size:4px;font-weight:600;color:var(--orange);margin-bottom:1px}
.card-dark{top:228px;width:78px;height:46px}
.card-black{left:12px;background:var(--card-dark)}
.card-orange{left:94px;background:linear-gradient(120deg,var(--orange-deep),var(--orange) 60%,var(--orange-light))}
.card-appt{left:176px;background:linear-gradient(180deg,#f4f4f4,#dcdcdc)}
.card-dark .line{position:absolute;left:6px;top:14px;width:34px;height:1px;background:rgba(255,255,255,.5)}
.card-appt .line{background:var(--ink-soft)}

/* letterheads */
.letterhead{top:22px;width:176px;height:242px;padding:12px 12px}
.lh-one{left:362px}
.lh-two{left:558px}
.letterhead .brand-mark{width:6px;height:6px}
.letterhead .brand-name{font-size:5px;width:70px}
.letterhead .contact{position:absolute;right:12px;top:12px;text-align:right}
.letterhead .edge{position:absolute;right:0;top:0;width:4px;height:20px;background:var(--orange)}
.letterhead .footer{position:absolute;left:12px;right:12px;bottom:8px;text-align:center}

/* envelopes */
.envelope{left:751px;width:170px;padding:6px 8px}
.env-large{top:52px;height:80px}
.env-small{top:156px;height:74px}
.envelope .brand-mark{width:5px;height:5px}
.envelope .brand-name{font-size:4px;width:60px}

/* open envelopes */
.folder{position:absolute;left:941px;top:58px;width:250px;height:124px}
</style>
</head>
<body>

<div class="hero-logo brand">
  <span class="brand-mark"></span>
  <div>
    <div class="brand-name">Lakeshore Vision Associates</div>
    <div class="tagline">Diseases and Surgeries of the Retina, Macula and Vitreous</div>
  </div>
</div>

<div class="piece card card-front">
  <div class="brand"><span class="brand-mark"></span><span class="brand-name">Lakeshore Vision Associates</span></div>
</div>
<div class="piece card card-back">
  <div class="name">Peter R. Haldane, MD</div>
  <div class="small">Birchwood Medical Tower<br>4215 N. Lindon Suite 812<br>Wexmore, IL 60952<br>peter@lakeshorevsa.com<br>www.lakeshorevsa.com</div>
</div>

<div class="piece card-dark card-black"><span class="line"></span></div>
<div class="piece card-dark card-orange"><span class="line"></span></div>
<div class="piece card-dark card-appt"><span class="line"></span></div>

<div class="piece letterhead lh-one">
  <span class="edge"></span>
  <div class="brand"><span class="brand-mark"></span><span class="brand-name">Lakeshore Vision Associates</span></div>
  <div class="contact small">Birchwood Medical Tower<br>4215 N. Lindon Suite 812<br>Wexmore, IL 60952</div>
</div>
<div class="piece letterhead lh-two">
  <span class="edge"></span>
  <div class="brand"><span class="brand-mark"></span><span class="brand-name">Lakeshore Vision Associates</span></div>
  <div class="footer small">Birchwood Medical Tower · 4215 N. Lindon Suite 812 · Wexmore, IL 60952 · www.lakeshorevsa.com</div>
</div>

<div class="piece envelope env-large">
  <div class="brand"><span class="brand-mark"></span><span class="brand-name">Lakeshore Vision Associates</span></div>
</div>
<div class="piece envelope env-small">
  <div class="brand"><span class="brand-mark"></span><span class="brand-name">Lakeshore Vision Associates</span></div>
</div>

<svg class="folder" viewBox="0 0 250 124" aria-hidden="true">
  <defs>
    <linearGradient id="flapOrange" x1="0" y1="0" x2="1" y2="1">
      <stop offset="0" stop-color="#fbb04a"/>
      <stop offset=".6" stop-color="#f07a14"/>
      <stop offset="1" stop-color="#c2470a"/>
    </linearGradient>
  </defs>
  <rect x="2" y="2" width="150" height="70" fill="url(#flapOrange)"/>
  <rect x="8" y="40" width="170" height="80" fill="#ffffff"/>
  <polygon points="8,40 178,40 93,82" fill="url(#flapOrange)"/>
  <rect x="110" y="30" width="136" height="64" fill="#f6f6f6"/>
  <polyline points="110,94 178,66 246,94" fill="none" stroke="#cfcfcf" stroke-width="1"/>
  <polygon points="110,30 246,30 178,60" fill="#e3e3e3"/>
  <polygon points="110,30 246,30 178,52" fill="#ffffff"/>
</svg>

</body>
</html>
```